Coffeeshop menu for filter tip

We want to have a cannabis (coffeeshop) menu in the size 25mm wide x 60mm wide. Some examples attached.

it must have the following text:
Menu

WEED p/g
Velotrine €16
Cinderfox €14
Tide Rambler €14
Marigolden €16
Grand Pelican €14
Copper Comet €14

HASH p/g
Baltic Ember €12
Harbor Velvet€11
Plum Rova €14
Dusk Maple €10

Target Market(s)

tourist in Amsterdam

Requirements
Nice to have
• cannabis sign leaf
• No Cigarettes allowed symbol

```html
<!DOCTYPE html>
<html lang="en">
<head>
<meta charset="utf-8">
<title>Coffeeshop Menu – Filter Tip</title>
<link href="https://fonts.googleapis.com/css2?family=Grenze:wght@700&family=Pacifico&family=Henny+Penny&family=Mystery+Quest&family=UnifrakturMaguntia&family=Lobster&family=Mouse+Memoirs&display=swap" rel="stylesheet">
<style>
  :root {
    --page: #ffffff;
    --leaf-green: #249a44;
    --leaf-dark: #11692b;
    --board-brown: #4a1e0c;
    --board-red: #8c1b12;
    --gold: #c9a227;
    --gold-light: #f0d36a;
    --ink: #ffffff;
  }
  * { margin: 0; padding: 0; box-sizing: border-box; }
  html, body { width: 845px; height: 1200px; overflow: hidden; background: var(--page); }
  .canvas { position: relative; width: 845px; height: 1200px; }

  .menu {
    position: absolute; left: 255px; top: 174px; width: 353px; height: 842px;
    overflow: hidden;
    background: radial-gradient(ellipse at 50% 45%, var(--leaf-green) 0%, var(--leaf-dark) 100%);
  }
  .leaf-pattern {
    position: absolute; inset: 0;
    background: repeating-radial-gradient(circle at 30% 30%, rgba(255,255,255,0.03) 0 30px, rgba(0,0,0,0.05) 30px 60px);
  }
  .ornament {
    position: absolute; left: 60px; width: 233px; height: 30px; border-radius: 15px;
    background: linear-gradient(90deg, transparent, var(--gold) 20%, var(--gold-light) 50%, var(--gold) 80%, transparent);
    opacity: 0.85;
  }
  .ornament--top { top: 6px; }
  .ornament--bottom { bottom: 8px; }

  .board {
    position: absolute; left: 8px; width: 337px; border-radius: 24px;
    background: radial-gradient(ellipse at 50% 50%, var(--board-red) 0%, var(--board-brown) 70%);
  }
  .board--weed { top: 118px; height: 350px; }
  .board--hash { top: 550px; height: 238px; }

  .heading {
    position: absolute; left: 0; width: 353px; text-align: center;
    font-family: "Mouse Memoirs", sans-serif; font-weight: 400;
    font-size: 84px; line-height: 70px; letter-spacing: 3px;
    color: var(--ink); white-space: nowrap;
  }
  .heading--weed { top: 44px; }
  .heading--hash { top: 474px; }

  .item {
    position: absolute; left: 12px; width: 331px; height: 54px;
    display: flex; align-items: center; justify-content: space-between;
  }
  .item__name { color: var(--ink); white-space: nowrap; line-height: 1; }
  .item__price {
    font-family: "Grenze", serif; font-weight: 700; font-size: 30px;
    color: var(--ink); line-height: 1; white-space: nowrap; padding-right: 4px;
  }

  .n1 { font-family: "Grenze", serif; font-weight: 700; font-size: 36px; letter-spacing: 1px; }
  .n2 { font-family: "Grenze", serif; font-weight: 700; font-size: 38px; }
  .n3 { font-family: "Mouse Memoirs", sans-serif; font-size: 40px; text-transform: uppercase; letter-spacing: 1px; }
  .n4 { font-family: "Pacifico", cursive; font-size: 30px; }
  .n5 { font-family: "Henny Penny", cursive; font-size: 31px; }
  .n6 { font-family: "Mystery Quest", cursive; font-size: 36px; }
  .n7 { font-family: "Lobster", cursive; font-size: 38px; }
  .n8 { font-family: "UnifrakturMaguntia", serif; font-size: 36px; }
  .n9 { font-family: "Grenze", serif; font-weight: 700; font-size: 38px; }
  .n10 { font-family: "Mouse Memoirs", sans-serif; font-size: 46px; }
</style>
</head>
<body>
<div class="canvas">
  <section class="menu" aria-label="Coffeeshop menu">
    <div class="leaf-pattern" role="img" aria-label="Cannabis leaf pattern background"></div>
    <div class="ornament ornament--top" role="img" aria-label="Gold scroll ornament"></div>
    <div class="board board--weed"></div>
    <div class="board board--hash"></div>

    <h2 class="heading heading--weed">WEED P/G</h2>
    <div class="item" style="top:116px"><span class="item__name n1">Velotrine</span><span class="item__price">€16</span></div>
    <div class="item" style="top:171px"><span class="item__name n2">Cinderfox</span><span class="item__price">€14</span></div>
    <div class="item" style="top:226px"><span class="item__name n3">Tide Rambler</span><span class="item__price">€14</span></div>
    <div class="item" style="top:280px"><span class="item__name n4">Marigolden</span><span class="item__price">€16</span></div>
    <div class="item" style="top:343px"><span class="item__name n5">Grand Pelican</span><span class="item__price">€14</span></div>
    <div class="item" style="top:406px"><span class="item__name n6">Copper Comet</span><span class="item__price">€14</span></div>

    <h2 class="heading heading--hash">HASH P/G</h2>
    <div class="item" style="top:552px"><span class="item__name n7">Baltic Ember</span><span class="item__price">€12</span></div>
    <div class="item" style="top:617px"><span class="item__name n8">Harbor Velvet</span><span class="item__price">€11</span></div>
    <div class="item" style="top:678px"><span class="item__name n9">Plum Rova</span><span class="item__price">€14</span></div>
    <div class="item" style="top:733px"><span class="item__name n10">Dusk Maple</span><span class="item__price">€10</span></div>

    <div class="ornament ornament--bottom" role="img" aria-label="Gold scroll ornament"></div>
  </section>
</div>
</body>
</html>
```